Business cards for start-up accounting firm

I'm looking for a double sided business card ready for upload into Prontel ink or similar print providers with no modification required by me.
I'm looking for something simple as i think cards that are too 'busy' actually detract from the message. I have some thoughts but more than happy to see what comes up. The logo i have came out of left field and i love it the moment i saw it!

My thoughts:

Side 1: Just the logo, perhaps on a dark grey or charcoal background to make the logo colours stand out?

Side 2: The call to action from me website 'Looking for a more relaxed, friendly and interactive relationship with your accountant?' with my contact information
Name: Gavin Ormsby
Email: gavin@quellorix.com.au
Website: www.quellorix.com.au
Phone: 1300 742 916

The call to action needs to be the first thing they see when they look at side 2. If it helps to know what we do and how we do it there is a draft website at www.quellorix.com.au

Like i said, happy to consider anything that comes up :)

Target Market(s)

i'm targeting small business owners who experience a lot of stress around finacial reporting and have had bad experiences with accountants in the past.

Industry/Entity Type

Accounting

Contact Information for Business Card

Contained in the Description

Font styles to use
Serif
Sans Serif
Other font styles liked:
• See logo files attached

Colors
474747

Requirements
Must have
• My logo, slogan and contact information

```html
<!DOCTYPE html>
<html lang="en">
<head>
<meta charset="UTF-8">
<title>Quellorix – Business Cards</title>
<link rel="stylesheet" href="https://fonts.googleapis.com/css2?family=Arimo:wght@400;700&display=swap">
<style>
  :root {
    --stage: #2e2e30;
    --plum: #8c2a80;
    --paper: #ffffff;
    --ink: #575757;
    --rule: #d9d2d8;
  }
  * { box-sizing: border-box; margin: 0; padding: 0; }
  html, body { width: 1200px; height: 950px; overflow: hidden; }
  body {
    background: var(--stage);
    font-family: "Arimo", Arial, sans-serif;
    position: relative;
  }
  .card {
    position: absolute;
    width: 680px;
    height: 416px;
    border-radius: 4px;
    box-shadow: 0 14px 30px rgba(0,0,0,0.45);
  }
  .brand__name {
    display: inline-flex; align-items: center; gap: 14px;
    font-weight: 700; line-height: 1;
    letter-spacing: 1px;
    color: currentColor;
  }
  .brand__dot {
    border-radius: 50%;
    background: currentColor;
  }

  /* Side 1 – call to action */
  .card--front {
    left: 190px; top: 40px;
    background: var(--plum);
    color: var(--paper);
    text-align: center;
  }
  .card--front .brand { margin-top: 110px; }
  .card--front .brand__name { font-size: 64px; }
  .card--front .brand__dot { width: 20px; height: 20px; }
  .cta {
    margin: 56px auto 0;
    width: 500px;
    font-size: 20px; line-height: 1.45;
  }

  /* Side 2 – contact */
  .card--back {
    left: 330px; top: 494px;
    background: var(--paper);
    display: flex; align-items: center;
  }
  .card--back .brand {
    width: 350px; margin-top: 60px;
    display: flex; justify-content: center;
    color: var(--plum);
  }
  .card--back .brand__name { font-size: 54px; }
  .card--back .brand__dot { width: 16px; height: 16px; }
  .divider {
    width: 1px; height: 160px; margin-top: -20px;
    background: linear-gradient(to bottom, transparent, var(--rule) 25%, var(--rule) 75%, transparent);
  }
  .contact { padding-left: 30px; margin-top: -60px; }
  .contact__name {
    color: var(--plum); font-size: 25px; font-weight: 400;
    margin-bottom: 10px;
  }
  .contact__list { list-style: none; }
  .contact__item {
    display: flex; align-items: center; gap: 9px;
    color: var(--ink); font-size: 17px; line-height: 1.5;
  }
  .contact__icon { width: 15px; height: 15px; fill: var(--plum); flex: none; }
</style>
</head>
<body>
  <section class="card card--front">
    <div class="brand">
      <div class="brand__name"><span>Quellorix</span><span class="brand__dot"></span></div>
    </div>
    <p class="cta">Looking for a more relaxed, friendly and interactive relationship with your accountant?</p>
  </section>

  <section class="card card--back">
    <div class="brand">
      <div class="brand__name"><span>Quellorix</span><span class="brand__dot"></span></div>
    </div>
    <div class="divider"></div>
    <div class="contact">
      <h2 class="contact__name">Gavin Ormsby</h2>
      <ul class="contact__list">
        <li class="contact__item">
          <svg class="contact__icon" viewBox="0 0 16 16" aria-hidden="true"><path d="M3.6 1.2l2.3 2.6-1.2 1.8c.9 2 2.6 3.7 4.6 4.6l1.8-1.2 2.6 2.3-1.4 2.5C7.1 15.2.8 8.9 1.1 3z"/></svg>
          1300 742 916
        </li>
        <li class="contact__item">
          <svg class="contact__icon" viewBox="0 0 16 16" aria-hidden="true"><path d="M1 3h14v1.2L8 9 1 4.2z"/><path d="M1 5.8l7 4.8 7-4.8V13H1z"/></svg>
          gavin@quellorix.com.au
        </li>
        <li class="contact__item">
          <svg class="contact__icon" viewBox="0 0 16 16" aria-hidden="true"><path d="M8 1a5 5 0 0 0-5 5c0 3.6 5 9 5 9s5-5.4 5-9a5 5 0 0 0-5-5zm0 7a2 2 0 1 1 0-4 2 2 0 0 1 0 4z"/></svg>
          quellorix.com.au
        </li>
      </ul>
    </div>
  </section>
</body>
</html>
```